" A empresa ainda é nova e irá trabalhar com projetos e obras para terceiros, estou querendo atuar principalmente em condomínio fechado na construções de casas. "

```html
<!DOCTYPE html>
<html lang="pt-BR">
<head>
<meta charset="UTF-8">
<title>VERTA Projetos e Construções – Envelope</title>
<link href="https://fonts.googleapis.com/css2?family=Montserrat:wght@400;600&display=swap" rel="stylesheet">
<style>
  :root {
    --backdrop: #e8e9ea;
    --paper: #ffffff;
    --navy: #0f2940;
    --navy-deep: #0b2036;
    --teal: #1aa3c4;
    --teal-dark: #138aa8;
    --ghost-light: #eef1f3;
    --ghost-dark: #17344f;
    --muted-light: #8c98a4;
    --muted-dark: #b9c7d3;
  }
  * { margin: 0; padding: 0; box-sizing: border-box; }
  html, body {
    width: 1200px; height: 1200px; overflow: hidden;
    background: var(--backdrop);
    font-family: "Montserrat", Arial, sans-serif;
  }
  .stationery {
    position: absolute; left: 156px; top: 283px;
    width: 888px; height: 634px;
    display: flex;
    box-shadow: 0 6px 18px rgba(0,0,0,0.18);
  }
  .envelope-face {
    position: relative; width: 444px; height: 634px; overflow: hidden;
  }
  .envelope-face--front { background: var(--paper); }
  .envelope-face--back { background: var(--navy); }

  .backdrop-shape {
    position: absolute; left: 96px; top: 120px; width: 252px; height: 460px;
  }
  .envelope-face--front .backdrop-shape {
    background: linear-gradient(180deg, var(--ghost-light) 0%, #f6f8f9 100%);
  }
  .envelope-face--back .backdrop-shape {
    left: 100px; top: 140px;
    background: linear-gradient(180deg, var(--ghost-dark) 0%, var(--navy) 100%);
  }

  .brand {
    position: absolute; left: 0; right: 0; text-align: center;
  }
  .brand-name {
    display: inline-flex; align-items: center; gap: 12px;
    font-weight: 600; color: var(--teal); letter-spacing: 4px;
  }
  .brand-dot { display: inline-block; background: var(--teal); }
  .brand-tagline {
    display: block; font-weight: 400; letter-spacing: 2.5px; margin-top: 6px;
  }
  .envelope-face--front .brand { top: 322px; }
  .envelope-face--front .brand-name { font-size: 52px; }
  .envelope-face--front .brand-dot { width: 18px; height: 18px; }
  .envelope-face--front .brand-tagline { font-size: 11px; color: var(--muted-light); }

  .envelope-face--back .brand { top: 466px; }
  .envelope-face--back .brand-name { font-size: 34px; }
  .envelope-face--back .brand-dot { width: 12px; height: 12px; }
  .envelope-face--back .brand-tagline { font-size: 7.5px; color: var(--muted-dark); }

  .flap { position: absolute; left: 0; top: 0; width: 444px; height: 66px; }
  .bottom-band { position: absolute; left: 0; bottom: 0; width: 444px; height: 26px; }

  .contact-line {
    position: absolute; left: 0; right: 0; top: 562px;
    display: flex; justify-content: center; gap: 22px;
    font-size: 7px; color: var(--muted-dark);
  }
  .contact-item { display: inline-flex; align-items: center; gap: 4px; }
  .contact-item svg { width: 8px; height: 8px; }
</style>
</head>
<body>
  <div class="stationery">
    <section class="envelope-face envelope-face--front">
      <div class="backdrop-shape" role="img" aria-label="Faint building silhouettes decoration"></div>
      <div class="brand">
        <span class="brand-name"><span class="brand-dot"></span>VERTA</span>
        <span class="brand-tagline">PROJETOS E CONSTRUÇÕES</span>
      </div>
      <svg class="bottom-band" viewBox="0 0 444 26" preserveAspectRatio="none">
        <polygon points="0,0 444,0 444,26 0,26" fill="var(--navy)"/>
        <polygon points="400,0 444,0 444,26 380,26" fill="var(--navy-deep)"/>
      </svg>
    </section>

    <section class="envelope-face envelope-face--back">
      <svg class="flap" viewBox="0 0 444 66" preserveAspectRatio="none">
        <path d="M0,0 H444 V38 Q444,66 416,66 H28 Q0,66 0,38 Z" fill="var(--teal)"/>
      </svg>
      <div class="backdrop-shape" role="img" aria-label="Faint building silhouettes decoration"></div>
      <div class="brand">
        <span class="brand-name"><span class="brand-dot"></span>VERTA</span>
        <span class="brand-tagline">PROJETOS E CONSTRUÇÕES</span>
      </div>
      <div class="contact-line">
        <span class="contact-item">Rua das Obras, 120 Centro
          <svg viewBox="0 0 10 10"><path d="M5 0.5a3 3 0 0 1 3 3c0 2.3-3 6-3 6s-3-3.7-3-6a3 3 0 0 1 3-3z" fill="var(--teal)"/></svg></span>
        <span class="contact-item">contato@vertaobras.com
          <svg viewBox="0 0 10 10"><rect x="0.5" y="2" width="9" height="6" fill="none" stroke="var(--teal)"/><path d="M0.5 2l4.5 3.5L9.5 2" fill="none" stroke="var(--teal)"/></svg></span>
        <span class="contact-item">(11) 4000-2000
          <svg viewBox="0 0 10 10"><path d="M2 1l2 2-1 1.2a6 6 0 0 0 2.8 2.8L7 6l2 2-1.3 1.3C4.5 9 1 5.5 0.7 2.3z" fill="var(--teal)"/></svg></span>
      </div>
      <svg class="bottom-band" viewBox="0 0 444 26" preserveAspectRatio="none">
        <polygon points="0,6 444,0 444,26 0,26" fill="var(--teal)"/>
        <polygon points="300,4 444,0 444,26 340,26" fill="var(--teal-dark)"/>
      </svg>
    </section>
  </div>
</body>
</html>
```